Website for Tech Venture Capital - Korvend Capital

We need a website for Korvend Capital.
Slogan:
Helping Ambitious Entrepreneurs Start and Build Great Companies.

Korvend Capital is a venture capital looking to support and invest in young talent within the technology and digital marketing industry. We wish for a website that reflects that while matching our logo and color palette.

Our Domain is: https://korvend.vc/
We would like to have these considered as references/inspiration for our website:
https://www.tilmorefund.com/
https://www.brunhalecap.com/israel/

You can find the desired structure and the zip file attached.
There is a color palette attached as well.
Social media pages to be used:
https://www.linkedin.com/in/jonmirtaveski/
https://www.linkedin.com/in/tomas-dune-rok/
https://www.linkedin.com/in/corvish/

Target Market(s)

Young Tech and Digital Marketing Entrepreneurs

Industry/Entity Type

Tech, Finance

Coding

Coded - Design and coding required

Number of Pages Required

4 page

Font styles to use
Sans Serif

Colors
0054AA
0677BA
7BADD7
CADEEF
E8F1F8
0094D4
00A9DD
6FCCEA
C7EBF8
E9F6FB

Requirements
Must have
• Please see attached files. WordPress sites strongly preferred.

```html
<!DOCTYPE html>
<html lang="en">
<head>
<meta charset="utf-8">
<title>Korvend Capital</title>
<link href="https://fonts.googleapis.com/css2?family=Poppins:wght@700&family=Roboto:wght@400;500;700&display=swap" rel="stylesheet">
<style>
:root{
  --navy:#141a4a;
  --navy-deep:#131b4f;
  --blue:#1a9bd7;
  --blue-light:#4cb5e5;
  --partner-bg:#1f3570;
  --text:#6b6f7a;
  --white:#ffffff;
  --line:#eef0f4;
}
*{margin:0;padding:0;box-sizing:border-box}
html,body{width:1200px;height:3245px;overflow:hidden}
body{font-family:"Roboto",sans-serif;color:var(--text);background:var(--white);position:relative}
.abs{position:absolute}
h1,h2,.display{font-family:"Poppins",sans-serif;font-weight:700}

/* header */
.site-header{position:absolute;top:0;left:0;width:1200px;height:76px;background:var(--white)}
.brand{left:111px;top:20px;font-family:"Roboto",sans-serif;font-weight:700;font-size:28px;color:#1e6fa8}
.main-nav{right:113px;top:29px;display:flex;gap:33px;font-size:14px;font-weight:500;color:#1b1f2e}
.main-nav .active{color:var(--blue)}

/* hero */
.hero{position:absolute;top:76px;left:0;width:1200px;height:556px;
  background:linear-gradient(100deg,#3a4650 0%,#2d3a44 35%,#1d4a66 55%,#3d7fa0 68%,#27485a 85%,#1c2a33 100%)}
.hero-title{left:110px;top:122px;font-size:53px;line-height:55px;color:var(--white);letter-spacing:-.3px}
.hero-title em{font-style:normal;color:var(--blue)}
.btn{display:flex;align-items:center;gap:10px;background:var(--blue);color:var(--white);font-weight:500;font-size:15px;padding:0 18px;height:48px;border-radius:2px}
.hero .btn{left:111px;top:377px}
.slide-arrow{top:258px;width:38px;height:38px;border-radius:50%;background:var(--white);display:flex;align-items:center;justify-content:center}

/* about */
.about{position:absolute;top:632px;left:0;width:1200px;height:592px}
.about-main-photo{left:111px;top:107px;width:359px;height:319px;border:5px solid #fff;box-shadow:0 2px 10px rgba(0,0,0,.18);border-radius:4px;
  background:linear-gradient(135deg,#5d87b4,#2f5f95 55%,#9bb4cc)}
.about-video{left:325px;top:268px;width:201px;height:203px;border:8px solid #fff;
  background:linear-gradient(160deg,#b8c8d6,#5f7f9a 60%,#2e4a66)}
.play{left:84px;top:85px;width:36px;height:36px}
.about h2{left:617px;top:110px;font-size:45px;color:var(--navy)}
.about-copy{left:617px;top:172px;width:460px;font-size:14.5px;line-height:25.7px}
.about-copy p+p{margin-top:26px}
.about .btn{left:617px;top:419px;height:48px}

/* partners */
.partners{position:absolute;top:1224px;left:0;width:1200px;height:590px;
  background:linear-gradient(180deg,#263b78,#1d3168 60%,#1f3570)}
.partners h2{left:0;width:1200px;text-align:center;top:62px;font-size:45px;color:var(--white)}
.partner-card{top:160px;width:312px;height:346px;background:var(--white);text-align:center}
.partner-photo{position:absolute;left:10px;top:8px;width:292px;height:243px}
.partner-link{position:absolute;left:136px;top:233px;width:40px;height:40px;border-radius:50%;background:var(--blue)}
.partner-name{position:absolute;left:0;width:100%;top:285px;font-weight:500;font-size:19px;color:#161821}
.partner-role{position:absolute;left:0;width:100%;top:314px;font-size:14px;color:#5b5f6a}

/* why choose */
.why{position:absolute;top:1814px;left:0;width:1200px;height:934px}
.why h2{left:0;width:1200px;text-align:center;top:76px;font-size:45px;color:var(--navy)}
.feature{width:316px;height:313px;background:var(--white);box-shadow:0 1px 8px rgba(0,0,0,.12)}
.feature-icon{position:absolute;left:19px;top:23px;width:94px;height:91px;background:var(--blue)}
.feature-title{position:absolute;left:137px;top:51px;font-size:16.5px;font-weight:500;color:#1b1d28}
.feature-title::after{content:"";position:absolute;left:0;top:32px;width:36px;height:2px;background:var(--blue)}
.feature-text{position:absolute;left:19px;top:135px;width:282px;font-size:14.3px;line-height:22.3px;color:var(--text)}
.feature-more{position:absolute;left:19px;top:262px;font-size:12.5px;font-weight:500;color:var(--blue);text-decoration:underline;display:flex;align-items:center;gap:8px}

/* newsletter */
.newsletter{position:absolute;top:2748px;left:0;width:1200px;height:217px;background:var(--blue-light)}
.newsletter h2{left:111px;top:52px;font-size:43px;color:var(--white)}
.newsletter p{left:111px;top:124px;width:430px;font-size:15px;line-height:24px;color:#e8f6fd}
.signup{left:603px;top:84px;width:484px;height:50px;background:var(--white);border:1px solid #e3e6ea;display:flex}
.signup .field{flex:1;display:flex;align-items:center;gap:12px;padding-left:22px;font-size:13.5px;color:#6c7078}
.signup .submit{width:144px;margin:2px;background:var(--navy-deep);color:var(--white);font-weight:700;font-size:14px;display:flex;align-items:center;justify-content:center}

/* footer */
.site-footer{position:absolute;top:2965px;left:0;width:1200px;height:280px;background:var(--navy-deep);color:var(--white)}
.footer-nav{left:0;width:1200px;top:52px;display:flex;justify-content:center;gap:33px;font-size:14px;font-weight:700}
.footer-rule{left:111px;top:96px;width:978px;height:1px;background:#4a5185}
.footer-brand{left:111px;top:148px;font-weight:700;font-size:28px}
.copyright{left:111px;top:198px;font-size:14px}
.footer-heading{top:146px;font-size:13.5px;font-weight:700;letter-spacing:.3px}
.footer-item{display:flex;gap:14px;font-size:14px;line-height:22px}
.social{width:34px;height:34px;border:2px solid var(--white);border-radius:2px}
</style>
</head>
<body>

<header class="site-header">
  <div class="abs brand">Korvend</div>
  <nav class="abs main-nav">
    <span class="active">HOME</span><span>ABOUT US</span><span>TEAM</span><span>OPERATING PARTNERS</span><span>PORTFOLIO</span><span>BLOG</span><span>CONTACT</span>
  </nav>
</header>

<section class="hero" role="img" aria-label="Photo of a businessman holding a smartphone with glowing communication icons">
  <h1 class="abs hero-title">Helping Ambitious<br>Entrepreneurs Start<br>and Build <em>Great</em><br>Companies.</h1>
  <div class="abs btn">GET STARTED
    <svg width="15" height="15" viewBox="0 0 16 16"><circle cx="8" cy="8" r="7.5" fill="#fff"/><path d="M6 4.5 9.5 8 6 11.5" stroke="#1a9bd7" stroke-width="2" fill="none"/></svg>
  </div>
  <div class="abs slide-arrow" style="left:34px"><svg width="14" height="14" viewBox="0 0 14 14"><path d="M9 2 4 7l5 5" stroke="#111" stroke-width="2" fill="none"/></svg></div>
  <div class="abs slide-arrow" style="left:1127px"><svg width="14" height="14" viewBox="0 0 14 14"><path d="m5 2 5 5-5 5" stroke="#111" stroke-width="2" fill="none"/></svg></div>
</section>

<section class="about">
  <div class="abs about-main-photo" role="img" aria-label="Team reviewing charts with business data overlays"></div>
  <div class="abs about-video" role="img" aria-label="Video thumbnail of people working with a tablet">
    <svg class="abs play" viewBox="0 0 36 36"><circle cx="18" cy="18" r="17" fill="#1a9bd7" stroke="#fff" stroke-width="2"/><path d="M14 11v14l11-7z" fill="#fff"/></svg>
  </div>
  <h2 class="abs">About Us</h2>
  <div class="abs about-copy">
    <p>We are a team of founders and seasoned professionals who have taken the entrepreneurial journey ourselves in starting and building successful companies. Now as investors, we are excited to help future entrepreneurs succeed and win.</p>
    <p>Our focus is on helping pre-seed and seed startups launch and scale their companies. We believe in investing in ambitious entrepreneurs and using our expertise in helping them launch and scale successful products and services.</p>
  </div>
  <div class="abs btn">LEARN MORE
    <svg width="15" height="15" viewBox="0 0 16 16"><circle cx="8" cy="8" r="7.5" fill="#fff"/><path d="M6 4.5 9.5 8 6 11.5" stroke="#1a9bd7" stroke-width="2" fill="none"/></svg>
  </div>
</section>

<section class="partners">
  <h2 class="abs">Our Partners</h2>
  <div class="abs partner-card" style="left:111px">
    <div class="partner-photo" role="img" aria-label="Portrait of Noel Corvish" style="background:linear-gradient(180deg,#ececea,#e2dcd8)"></div>
    <div class="partner-link"></div>
    <div class="partner-name">Noel Corvish</div>
    <div class="partner-role">General Partner</div>
  </div>
  <div class="abs partner-card" style="left:444px">
    <div class="partner-photo" role="img" aria-label="Portrait of Tomas Dune-Rok" style="background:linear-gradient(180deg,#f0efed,#3b3d42)"></div>
    <div class="partner-link"></div>
    <div class="partner-name">Tomas Dune-Rok</div>
    <div class="partner-role">General Partner</div>
  </div>
  <div class="abs partner-card" style="left:777px">
    <div class="partner-photo" role="img" aria-label="Portrait of Jon Mirtaveski" style="background:linear-gradient(180deg,#b9a88f,#6b7f9a)"></div>
    <div class="partner-link"></div>
    <div class="partner-name">Jon Mirtaveski</div>
    <div class="partner-role">General Partner</div>
  </div>
</section>

<section class="why">
  <h2 class="abs">Why Choose Us</h2>

  <div class="abs feature" style="left:103px;top:173px">
    <div class="feature-icon" role="img" aria-label="Icon of a consultant with ideas"></div>
    <div class="feature-title">Lorem ipsum dolor sit</div>
    <p class="feature-text">Sed ut perspiciatis unde omnis iste natus error sit voluptatem accusanti doloremque laudantium, totam rem aperiaperspiciatis unde omnis iste natus error sit voluptatem accusanti doloremque laudantium</p>
    <div class="feature-more">LEARN MORE <svg width="12" height="12" viewBox="0 0 16 16"><circle cx="8" cy="8" r="7.5" fill="#1a9bd7"/><path d="M6 4.5 9.5 8 6 11.5" stroke="#fff" stroke-width="2" fill="none"/></svg></div>
  </div>
  <div class="abs feature" style="left:442px;top:173px">
    <div class="feature-icon" role="img" aria-label="Icon of a team group"></div>
    <div class="feature-title">Lorem ipsum dolor sit</div>
    <p class="feature-text">Sed ut perspiciatis unde omnis iste natus error sit voluptatem accusanti doloremque laudantium, totam rem aperiaperspiciatis unde omnis iste natus error sit voluptatem accusanti doloremque laudantium</p>
    <div class="feature-more">LEARN MORE <svg width="12" height="12" viewBox="0 0 16 16"><circle cx="8" cy="8" r="7.5" fill="#1a9bd7"/><path d="M6 4.5 9.5 8 6 11.5" stroke="#fff" stroke-width="2" fill="none"/></svg></div>
  </div>
  <div class="abs feature" style="left:781px;top:173px">
    <div class="feature-icon" role="img" aria-label="Icon of a briefcase"></div>
    <div class="feature-title">Lorem ipsum dolor sit</div>
    <p class="feature-text">Sed ut perspiciatis unde omnis iste natus error sit voluptatem accusanti doloremque laudantium, totam rem aperiaperspiciatis unde omnis iste natus error sit voluptatem accusanti doloremque laudantium</p>
    <div class="feature-more">LEARN MORE <svg width="12" height="12" viewBox="0 0 16 16"><circle cx="8" cy="8" r="7.5" fill="#1a9bd7"/><path d="M6 4.5 9.5 8 6 11.5" stroke="#fff" stroke-width="2" fill="none"/></svg></div>
  </div>

  <div class="abs feature" style="left:103px;top:518px">
    <div class="feature-icon" role="img" aria-label="Icon of a business person"></div>
    <div class="feature-title">Lorem ipsum dolor sit</div>
    <p class="feature-text">Sed ut perspiciatis unde omnis iste natus error sit voluptatem accusanti doloremque laudantium, totam rem aperiaperspiciatis unde omnis iste natus error sit voluptatem accusanti doloremque laudantium</p>
    <div class="feature-more">LEARN MORE <svg width="12" height="12" viewBox="0 0 16 16"><circle cx="8" cy="8" r="7.5" fill="#1a9bd7"/><path d="M6 4.5 9.5 8 6 11.5" stroke="#fff" stroke-width="2" fill="none"/></svg></div>
  </div>
  <div class="abs feature" style="left:442px;top:518px">
    <div class="feature-icon" role="img" aria-label="Icon of a person presenting growth data"></div>
    <div class="feature-title">Lorem ipsum dolor sit</div>
    <p class="feature-text">Sed ut perspiciatis unde omnis iste natus error sit voluptatem accusanti doloremque laudantium, totam rem aperiaperspiciatis unde omnis iste natus error sit voluptatem accusanti doloremque laudantium</p>
    <div class="feature-more">LEARN MORE <svg width="12" height="12" viewBox="0 0 16 16"><circle cx="8" cy="8" r="7.5" fill="#1a9bd7"/><path d="M6 4.5 9.5 8 6 11.5" stroke="#fff" stroke-width="2" fill="none"/></svg></div>
  </div>
  <div class="abs feature" style="left:781px;top:518px">
    <div class="feature-icon" role="img" aria-label="Icon of a businessman with a briefcase"></div>
    <div class="feature-title">Lorem ipsum dolor sit</div>
    <p class="feature-text">Sed ut perspiciatis unde omnis iste natus error sit voluptatem accusanti doloremque laudantium, totam rem aperiaperspiciatis unde omnis iste natus error sit voluptatem accusanti doloremque laudantium</p>
    <div class="feature-more">LEARN MORE <svg width="12" height="12" viewBox="0 0 16 16"><circle cx="8" cy="8" r="7.5" fill="#1a9bd7"/><path d="M6 4.5 9.5 8 6 11.5" stroke="#fff" stroke-width="2" fill="none"/></svg></div>
  </div>
</section>

<section class="newsletter">
  <h2 class="abs">Join Our Newsletter</h2>
  <p class="abs">Sed ut perspiciatis unde omnis iste natus error sit voluptatem accusantium doloremque laudantium, totam</p>
  <div class="abs signup">
    <div class="field">
      <svg width="14" height="11" viewBox="0 0 14 11"><rect x=".5" y=".5" width="13" height="10" fill="#6c7078"/><path d="M.5 .8 7 6l6.5-5.2" stroke="#fff" fill="none"/></svg>
      Enter Your Email Address
    </div>
    <div class="submit">SUBSCRIBE</div>
  </div>
</section>

<footer class="site-footer">
  <nav class="abs footer-nav">
    <span>HOME</span><span>ABOUT US</span><span>TEAM</span><span>OPERATING PARTNERS</span><span>PORTFOLIO</span><span>BLOG</span><span>CONTACT</span>
  </nav>
  <div class="abs footer-rule"></div>
  <div class="abs footer-brand">Korvend</div>
  <div class="abs copyright">© 2021 Korvend Capital. All Rights Reserved</div>

  <div class="abs footer-heading" style="left:457px">OFFICE LOCATION</div>
  <div class="abs footer-item" style="left:457px;top:175px">
    <svg width="10" height="14" viewBox="0 0 10 14" style="margin-top:4px"><path d="M5 0a5 5 0 0 0-5 5c0 3.5 5 9 5 9s5-5.5 5-9a5 5 0 0 0-5-5z" fill="#fff"/><circle cx="5" cy="5" r="1.8" fill="#131b4f"/></svg>
    <span>Westbrook 48 Harlan Street<br>United States</span>
  </div>

  <div class="abs footer-heading" style="left:758px">CONTACT US</div>
  <div class="abs footer-item" style="left:758px;top:175px;font-size:16px;font-weight:700">
    <svg width="14" height="14" viewBox="0 0 14 14" style="margin-top:4px"><path d="M3 0 5 3.5 3.5 5C4.5 7 7 9.5 9 10.5L10.5 9 14 11l-1.5 3C6 14 0 8 0 1.5z" fill="#fff"/></svg>
    <span style="margin-left:4px">1 555 010 2040</span>
  </div>
  <div class="abs footer-item" style="left:758px;top:206px">
    <svg width="14" height="11" viewBox="0 0 14 11" style="margin-top:6px"><rect width="14" height="11" fill="#fff"/><path d="M0 .5 7 6l7-5.5" stroke="#131b4f" fill="none"/></svg>
    <span style="margin-left:4px">contact@korvend.vc</span>
  </div>

  <div class="abs social" style="left:981px;top:145px"></div>
  <div class="abs social" style="left:1024px;top:145px"></div>
  <div class="abs social" style="left:981px;top:188px"></div>
  <div class="abs social" style="left:1024px;top:188px"></div>
</footer>

</body>
</html>
```